Electrician's Business needs web site for customers to get professional impression of business.

Have a logo, need a web page for customers to visit. Web page should make it easy for customers to approach /contact me, if possible a way for customers to leave their details so I can call them back.
A description/ list of services and advertise how my service is different and better than other electricians.
A gallery to upload photos to, to show completed works from past projects.

Target Market(s)

Domestic/residential home owner/renter/builder

Industry/Entity Type

Electrician

Coding

Coded - Design and coding required

Number of Pages Required

2 page

Font styles to use
Sans Serif

Colors
0255a3
ffffff

Requirements
Must have
• Appeal to home owner/renter, domestic market.
• Capture contact details of customer & advertise my contact details.
• List of services
Nice to have
• A photo gallery, so I can upload pictures of completed work.
Should not have
• Industrial/construction images.

```html
<!DOCTYPE html>
<html lang="en">
<head>
<meta charset="utf-8">
<title>Brightwire Electrical Services</title>
<link rel="stylesheet" href="https://fonts.googleapis.com/css2?family=Exo+2:wght@400;500;600;700&display=swap">
<style>
  :root {
    --brand-blue: #0255a3;
    --white: #ffffff;
    --ink: #2b2b2b;
    --muted: #666666;
    --page-grey: #eeeeee;
    --hero-deep: #1a0f2e;
    --hero-magenta: #8a1a6a;
    --hero-violet: #3a1a5c;
  }
  * { box-sizing: border-box; margin: 0; padding: 0; }
  html, body {
    width: 1200px;
    height: 900px;
    overflow: hidden;
    background: var(--page-grey);
    font-family: "Exo 2", "Helvetica Neue", Arial, sans-serif;
  }
  .site {
    position: relative;
    width: 1200px;
    height: 900px;
    overflow: hidden;
  }

  /* Header */
  .site-header {
    position: absolute;
    top: 0; left: 0;
    width: 100%;
    height: 86px;
    background: var(--brand-blue);
    color: var(--white);
  }
  .brand {
    position: absolute;
    left: 110px;
    top: 26px;
    display: flex;
    align-items: center;
    gap: 10px;
  }
  .brand-mark {
    width: 14px;
    height: 14px;
    background: var(--white);
    border-radius: 50%;
  }
  .brand-name {
    font-weight: 700;
    font-size: 30px;
    line-height: 1;
    letter-spacing: 0.2px;
  }
  .header-call {
    position: absolute;
    right: 40px;
    top: 14px;
    font-size: 12px;
    color: #c9d8ea;
    text-decoration: underline;
  }
  .main-nav a {
    position: absolute;
    top: 50px;
    color: var(--white);
    text-decoration: none;
    font-size: 13px;
    font-weight: 600;
    letter-spacing: 0.5px;
  }
  .nav-home { left: 703px; }
  .nav-services { left: 804px; }
  .nav-work { left: 948px; }
  .nav-contact { left: 1050px; }

  /* Hero */
  .hero {
    position: absolute;
    top: 86px; left: 0;
    width: 100%;
    height: 612px;
  }
  .hero-image {
    position: absolute;
    inset: 0;
    background:
      radial-gradient(ellipse at 30% 40%, rgba(200,40,140,0.55), transparent 55%),
      radial-gradient(ellipse at 75% 30%, rgba(120,60,200,0.5), transparent 55%),
      radial-gradient(ellipse at 60% 85%, rgba(220,60,120,0.45), transparent 60%),
      linear-gradient(135deg, var(--hero-deep), var(--hero-violet) 45%, var(--hero-magenta));
  }
  .hero-content {
    position: absolute;
    top: 190px;
    left: 0;
    width: 100%;
    text-align: center;
    color: var(--white);
  }
  .hero-title {
    font-size: 46px;
    font-weight: 500;
    line-height: 56px;
    letter-spacing: -0.3px;
  }
  .hero-button {
    display: inline-block;
    margin-top: 20px;
    width: 218px;
    height: 46px;
    line-height: 44px;
    border: 1px solid rgba(255,255,255,0.85);
    color: var(--white);
    text-decoration: none;
    font-size: 14px;
    letter-spacing: 0.5px;
  }

  /* Services */
  .services-panel {
    position: absolute;
    top: 610px;
    left: 33px;
    width: 1134px;
    height: 290px;
    background: var(--white);
    text-align: center;
    padding-top: 30px;
  }
  .section-title {
    display: inline-block;
    font-size: 36px;
    font-weight: 600;
    line-height: 1.1;
    color: var(--ink);
    padding-bottom: 6px;
    border-bottom: 3px solid var(--ink);
  }
  .service-list {
    list-style: none;
    position: absolute;
    top: 116px;
    left: 0;
    width: 100%;
  }
  .service-item {
    position: absolute;
    top: 0;
    width: 280px;
    margin-left: -140px;
    text-align: center;
  }
  .service-item:nth-child(1) { left: 243px; }
  .service-item:nth-child(2) { left: 574px; }
  .service-item:nth-child(3) { left: 892px; }
  .service-icon {
    display: block;
    width: 52px;
    height: 52px;
    margin: 0 auto 12px;
  }
  .service-name {
    font-size: 20px;
    font-weight: 600;
    color: var(--brand-blue);
    margin-bottom: 6px;
  }
  .service-text {
    font-size: 14px;
    line-height: 20px;
    color: var(--muted);
  }
</style>
</head>
<body>
  <div class="site">
    <header class="site-header">
      <div class="brand">
        <span class="brand-mark"></span>
        <span class="brand-name">Brightwire</span>
      </div>
      <a class="header-call">Call Us Now</a>
      <nav class="main-nav">
        <a class="nav-home" href="#">HOME</a>
        <a class="nav-services" href="#">SERVICES</a>
        <a class="nav-work" href="#">WORK</a>
        <a class="nav-contact" href="#">CONTACT</a>
      </nav>
    </header>

    <section class="hero">
      <div class="hero-image" role="img" aria-label="Long-exposure photograph of colourful neon light trails in pink, yellow and blue"></div>
      <div class="hero-content">
        <h1 class="hero-title">Quality Installers, experts at fault finding!</h1>
        <a class="hero-button" href="#">ENQUIRE NOW</a>
      </div>
    </section>

    <section class="services-panel">
      <h2 class="section-title">Services</h2>
      <ul class="service-list">
        <li class="service-item">
          <svg class="service-icon" viewBox="0 0 52 52" aria-hidden="true">
            <circle cx="26" cy="26" r="26" fill="#0255a3"/>
            <path d="M15 27 L23 35 L38 18" fill="none" stroke="#ffffff" stroke-width="4" stroke-linecap="round" stroke-linejoin="round"/>
          </svg>
          <h3 class="service-name">Installations</h3>
          <p class="service-text">New power points, lighting and switchboards for your home.</p>
        </li>
        <li class="service-item">
          <svg class="service-icon" viewBox="0 0 52 52" aria-hidden="true">
            <circle cx="26" cy="26" r="26" fill="#0255a3"/>
            <path d="M15 27 L23 35 L38 18" fill="none" stroke="#ffffff" stroke-width="4" stroke-linecap="round" stroke-linejoin="round"/>
          </svg>
          <h3 class="service-name">Fault Finding</h3>
          <p class="service-text">Fast, accurate diagnosis of tripping, flickering and dead circuits.</p>
        </li>
        <li class="service-item">
          <svg class="service-icon" viewBox="0 0 52 52" aria-hidden="true">
            <circle cx="26" cy="26" r="26" fill="#0255a3"/>
            <path d="M15 27 L23 35 L38 18" fill="none" stroke="#ffffff" stroke-width="4" stroke-linecap="round" stroke-linejoin="round"/>
          </svg>
          <h3 class="service-name">Rewiring &amp; Upgrades</h3>
          <p class="service-text">Safe, compliant rewiring for older homes and renovations.</p>
        </li>
      </ul>
    </section>
  </div>
</body>
</html>
```